Harbor Nightclub

Nightclub flyer., digital single sided, for KV and PX. I included samples of some previous flyers we've used. Sample Info:
HARBOR
FRIDAYS
FRI MAY 1 2020
DJ VORTAN (club floor)
DJ RUZO & DJ TAV (residents on the lounge floor)
4217 Marlow Avenue Sacramento
www.harborvenuehall.example for list/VIP inquiries

Target Market(s)

Upscale top 40 crowd but want some cool and artsy like the examples included.

Font styles to use
Sans Serif

Requirements
Must have
• Harbor Logo
Nice to have
• Would be nice if the flyer can be incorporated later with DJ photos (sometimes we will add dj photos to pixagram etc). Would like a big city type of feel.
Should not have
• Nothing too sexual.

```html
<!DOCTYPE html>
<html lang="en">
<head>
<meta charset="utf-8">
<title>Harbor Fridays – Flyer</title>
<link rel="stylesheet" href="https://fonts.googleapis.com/css2?family=Montserrat:wght@300;400;600;700&family=Questrial&display=swap">
<style>
  :root {
    --bg-glow: #f6ecec;
    --bg-mid: #e2e0e0;
    --bg-edge: #b8b8b8;
    --ink: #111111;
    --title-dark: #0b0b10;
    --title-purple: #241046;
    --title-blue: #2fa8e6;
    --card: #ffffff;
    --logo-ink: #5a554c;
    --logo-dot: #d6cf6a;
  }
  html, body {
    margin: 0;
    padding: 0;
    overflow: hidden;
  }
  .flyer {
    position: relative;
    width: 933px;
    height: 1200px;
    overflow: hidden;
    font-family: "Montserrat", sans-serif;
    color: var(--ink);
    background:
      radial-gradient(ellipse 430px 420px at 466px 470px, var(--bg-glow) 0%, rgba(246,236,236,0.6) 35%, rgba(226,224,224,0) 75%),
      linear-gradient(180deg, #f7f7f7 0%, var(--bg-mid) 35%, #cfcfcf 75%, var(--bg-edge) 100%);
  }

  /* Logo card */
  .logo-card {
    position: absolute;
    left: 52px;
    top: 26px;
    width: 123px;
    height: 147px;
    background: var(--card);
    box-shadow: 1px 2px 3px rgba(0,0,0,0.35);
    display: flex;
    flex-direction: column;
    align-items: center;
    justify-content: center;
    gap: 12px;
  }
  .logo-mark {
    width: 34px;
    height: 34px;
    border-radius: 50%;
    background: var(--logo-dot);
  }
  .logo-name {
    font-family: "Montserrat", sans-serif;
    font-weight: 400;
    font-size: 19px;
    letter-spacing: 0.02em;
    color: var(--logo-ink);
  }

  .event-date {
    position: absolute;
    right: 56px;
    top: 52px;
    font-family: "Montserrat", sans-serif;
    font-weight: 400;
    font-size: 29px;
    letter-spacing: 0.01em;
  }

  /* Title */
  .title {
    position: absolute;
    left: 0;
    width: 100%;
    text-align: center;
    font-family: "Questrial", sans-serif;
    line-height: 1;
  }
  .title span {
    background:
      linear-gradient(118deg, transparent 30%, rgba(47,168,230,0.9) 31.5%, transparent 33%),
      linear-gradient(62deg, transparent 58%, rgba(47,168,230,0.85) 59.5%, transparent 61%),
      linear-gradient(90deg, var(--title-dark) 0%, var(--title-purple) 45%, var(--title-purple) 60%, var(--title-dark) 100%);
    -webkit-background-clip: text;
    background-clip: text;
    color: transparent;
  }
  .title-main {
    top: 448px;
    font-size: 166px;
    letter-spacing: 0.005em;
  }
  .title-sub {
    top: 578px;
    font-size: 136px;
  }

  /* Lineup */
  .music-by {
    position: absolute;
    top: 828px;
    width: 100%;
    text-align: center;
    font-weight: 700;
    font-size: 21px;
    letter-spacing: 0.32em;
  }
  .lineup {
    position: absolute;
    top: 876px;
    left: 0;
    width: 100%;
    display: flex;
    justify-content: center;
    align-items: flex-start;
    gap: 18px;
    font-size: 35px;
    letter-spacing: -0.03em;
  }
  .lineup .dj { font-weight: 700; }
  .lineup .name { font-weight: 300; }
  .lineup .divider { font-weight: 400; }
  .floor {
    display: flex;
    flex-direction: column;
  }
  .floor-right { align-items: flex-end; }
  .floor-note {
    font-weight: 300;
    font-size: 14px;
    letter-spacing: -0.02em;
    margin-top: 2px;
  }

  .address {
    position: absolute;
    top: 1003px;
    width: 100%;
    text-align: center;
    font-weight: 600;
    font-size: 18px;
    letter-spacing: 0.2em;
  }
  .separator {
    position: absolute;
    top: 1040px;
    width: 100%;
    text-align: center;
    font-size: 14px;
    letter-spacing: 0.5em;
    font-weight: 600;
  }
  .website {
    position: absolute;
    top: 1087px;
    width: 100%;
    text-align: center;
    font-weight: 600;
    font-size: 19px;
    letter-spacing: 0.3em;
  }
</style>
</head>
<body>
  <main class="flyer">
    <div class="logo-card">
      <div class="logo-mark"></div>
      <div class="logo-name">HARBOR</div>
    </div>

    <div class="event-date">FRI MAY 1 2020</div>

    <h1 class="title title-main"><span>HARBOR</span></h1>
    <h2 class="title title-sub"><span>FRIDAYS</span></h2>

    <div class="music-by">MUSIC BY:</div>

    <div class="lineup">
      <div class="floor floor-left">
        <div><span class="dj">DJ</span> <span class="name">VORTAN</span></div>
        <div class="floor-note">(CLUB FLOOR)</div>
      </div>
      <div class="divider">|</div>
      <div class="floor floor-right">
        <div><span class="dj">DJ</span> <span class="name">RUZO &amp;</span> <span class="dj">DJ</span> <span class="name">TAV</span></div>
        <div class="floor-note">(RESIDENTS ON THE LOUNGE FLOOR)</div>
      </div>
    </div>

    <div class="address">4217 MARLOW AVENUE SACRAMENTO</div>
    <div class="separator">·······</div>
    <div class="website">www.harborvenuehall.example for list/VIP inquiries</div>
  </main>
</body>
</html>
```